Financial Advisor Business Card

This business card is mainly a card for me personally (Marcus Tellavino) providing services as a Financial Planner and Accountant. My title is: Worth.while Mentor
Details provided about Harbourline Wealth Partners on the reverse side of the card is not dominant information, it is provided for ease of contact/communication purposes for prospective clients.
About me: I provide financial advice to my clients however due to regulatory issues in my industry I cannot use the title "Financial Advisor".
Target market is 25 y/o and onwards projecting a cutting edge, innovative and modern marketing influence.
Target Market(s)
25 years old and older
Industry/Entity Type
Financial
Contact Information for Business Card
Front side of business card
Name: Marcus Tellavino
Position: Worth.while Mentor
Accreditations:
Dip FS(FP)
B.Comm
Mobile: 0438 729 507
e-mail: mt@harbourwp.com.au
website: www.harbourwp.com.au
Reverse side of business card
Name: Marcus Tellavino
Company: Harbourline Wealth Partners
Position: Senior Accountant
Address:
Level 6, Suite 4
47 Gullwing Street
PO Box 872
MARROWVALE NSW 2391
Phone: (02) 49175381
Requirements
Must have
- - Cutting edge, innovative, fun but professional, modern marketing design and fonts
- Professional and legible
- Futuristic sharp lines, some with rounded edges
- Preferred Front Card colour scheme: Black background, Silver Text, White Text, Red & Silver lines
- Preferred Reverse Card colour scheme: White background, Silver Text, Black Text, Aqua & Silver lines
Nice to have
- Design a cutting edge logo of my intials as capital letters: MT
with a bigger D and smaller K - Preferred colour is Silver Text
Should not have
- Must not be:
- vintage/classic
- stereotypical accountant/tax agent/money style business card
- old style fonts e.g. times new roman

```html
<!DOCTYPE html>
<html lang="en">
<head>
<meta charset="utf-8">
<title>MT Business Card</title>
<link href="https://fonts.googleapis.com/css2?family=Ubuntu:wght@300;400;500;700&display=swap" rel="stylesheet">
<style>
  :root {
    --backdrop: #c9c9c9;
    --front-bg: #262626;
    --front-bg-deep: #161616;
    --back-bg: #ffffff;
    --red: #e0262b;
    --blue: #1e8fe0;
    --silver: #c8ccd0;
    --silver-dark: #8a9096;
    --white: #ffffff;
    --ink: #2b2b2b;
  }
  html, body {
    margin: 0;
    width: 1200px;
    height: 861px;
    overflow: hidden;
    background: var(--backdrop);
    font-family: "Ubuntu", sans-serif;
  }
  .stage {
    position: relative;
    width: 1200px;
    height: 861px;
  }
  .card {
    position: absolute;
    top: 275px;
    width: 540px;
    height: 310px;
    overflow: hidden;
    box-shadow: 0 6px 18px rgba(0,0,0,0.25);
  }
  .card--front { left: 50px; background: linear-gradient(135deg, var(--front-bg), var(--front-bg-deep)); }
  .card--back { left: 610px; background: var(--back-bg); }
  .card__bands {
    position: absolute;
    inset: 0;
    width: 540px;
    height: 310px;
  }
  .monogram {
    position: absolute;
    left: 290px;
    top: 58px;
    font-size: 84px;
    font-weight: 300;
    letter-spacing: 2px;
    line-height: 1;
    color: var(--silver);
  }
  .card--back .monogram { color: var(--silver-dark); }
  .identity {
    position: absolute;
    right: 250px;
    text-align: right;
  }
  .card--front .identity { top: 150px; }
  .card--back .identity { top: 145px; }
  .identity__name {
    font-size: 24px;
    font-weight: 700;
    white-space: nowrap;
    line-height: 1.1;
  }
  .card--front .identity__name { color: var(--red); }
  .card--back .identity__name { color: var(--blue); }
  .identity__title {
    font-size: 14px;
    font-weight: 500;
    margin-top: 2px;
  }
  .card--front .identity__title { color: var(--white); }
  .card--back .identity__title { color: var(--ink); }
  .details {
    position: absolute;
    margin: 0;
    white-space: nowrap;
  }
  .card--front .details { top: 212px; left: 150px; font-size: 12px; line-height: 16px; color: var(--white); }
  .card--back .details { top: 200px; left: 150px; font-size: 11px; line-height: 14px; color: var(--ink); }
  .details__row { display: flex; gap: 5px; }
  .details__label { font-weight: 700; text-align: right; width: 95px; margin: 0; }
  .details__value { margin: 0; }
  .card--front .details__label { color: var(--red); }
  .card--back .details__label { color: var(--blue); width: 60px; }
</style>
</head>
<body>
<main class="stage">

  <section class="card card--front" aria-label="Card front">
    <svg class="card__bands" viewBox="0 0 540 310" aria-hidden="true">
      <defs>
        <linearGradient id="red-edge" x1="0" x2="1" y1="0" y2="0">
          <stop offset="0" stop-color="#e0262b"/>
          <stop offset="1" stop-color="#ffffff"/>
        </linearGradient>
      </defs>
      <polygon points="320,0 364,0 444,44 540,120 540,150 420,55" fill="#f6d3d3"/>
      <polygon points="364,0 408,0 468,33 540,90 540,120 444,44" fill="#f09a9a"/>
      <polygon points="408,0 452,0 492,22 540,60 540,90 468,33" fill="#e96464"/>
      <polygon points="452,0 496,0 516,11 540,30 540,60 492,22" fill="#de3a3c"/>
      <polygon points="496,0 540,0 540,30 516,11" fill="#c71f24"/>
      <rect x="0" y="150" width="24" height="160" fill="url(#red-edge)"/>
    </svg>
    <div class="monogram">MT</div>
    <div class="identity">
      <div class="identity__name">Marcus Tellavino</div>
      <div class="identity__title">Worth.while Mentor</div>
    </div>
    <dl class="details">
      <div class="details__row"><dt class="details__label">Accreditations:</dt><dd class="details__value">Dip FS(FP) B.Comm</dd></div>
      <div class="details__row"><dt class="details__label">Mobile:</dt><dd class="details__value">0438 729 507</dd></div>
      <div class="details__row"><dt class="details__label">E-mail:</dt><dd class="details__value">mt@harbourwp.com.au</dd></div>
      <div class="details__row"><dt class="details__label">Website:</dt><dd class="details__value">www.harbourwp.com.au</dd></div>
    </dl>
  </section>

  <section class="card card--back" aria-label="Card back">
    <svg class="card__bands" viewBox="0 0 540 310" aria-hidden="true">
      <defs>
        <linearGradient id="blue-edge" x1="0" x2="1" y1="0" y2="0">
          <stop offset="0" stop-color="#1e8fe0"/>
          <stop offset="1" stop-color="#ffffff"/>
        </linearGradient>
      </defs>
      <polygon points="320,0 364,0 444,44 540,120 540,150 420,55" fill="#d4ebfb"/>
      <polygon points="364,0 408,0 468,33 540,90 540,120 444,44" fill="#9ccff4"/>
      <polygon points="408,0 452,0 492,22 540,60 540,90 468,33" fill="#62b2ec"/>
      <polygon points="452,0 496,0 516,11 540,30 540,60 492,22" fill="#2f95e2"/>
      <polygon points="496,0 540,0 540,30 516,11" fill="#1677c8"/>
      <rect x="0" y="150" width="24" height="160" fill="url(#blue-edge)"/>
    </svg>
    <div class="monogram">MT</div>
    <div class="identity">
      <div class="identity__name">Marcus Tellavino</div>
      <div class="identity__title">Worth.while Mentor</div>
    </div>
    <dl class="details">
      <div class="details__row"><dt class="details__label">Company:</dt><dd class="details__value">Harbourline Wealth Partners</dd></div>
      <div class="details__row"><dt class="details__label">Position:</dt><dd class="details__value">Senior Accountant</dd></div>
      <div class="details__row"><dt class="details__label">Address:</dt><dd class="details__value">Level 6, Suite 4, 47 Gullwing Street</dd></div>
      <div class="details__row"><dt class="details__label"></dt><dd class="details__value">PO Box 872 Marrowvale NSW 2391</dd></div>
      <div class="details__row"><dt class="details__label">Phone:</dt><dd class="details__value">(02) 49175381</dd></div>
      <div class="details__row"><dt class="details__label">E-mail:</dt><dd class="details__value">mt@harbourwp.com.au</dd></div>
      <div class="details__row"><dt class="details__label">Website:</dt><dd class="details__value">www.harbourwp.com.au</dd></div>
    </dl>
  </section>

</main>
</body>
</html>
```